New business cards for our company ORQEL

We need a new business card design for our existing company. We are a consulting/engineering firm which mainly works in the utility business. We would like to see designs which are pretty traditional and simple, with our logo, maybe with an option of a QR code on the back. We plan on using traditional rectangular horizontal format. Want our logo to be in red as attached, then company info in black or blue. I think we want a clean white card, no full color cards. Website is www.orqel-example.com.

Industry/Entity Type

Business

Contact Information for Business Card

Want a rectangular horizontal business card layout. Probably want a traditional layout with company logo on top right or top left, but open to new ideas. Will want to show company name, address, web address, phone, employee name and title.

Colors
ec1f27
0355a3
ffffff

Requirements
Must have
• business card design,
Nice to have
• QR code on back,
Should not have
• solid back ground card, want white back ground

```html
<!DOCTYPE html>
<html lang="en">
<head>
<meta charset="utf-8">
<title>ORQEL Business Card</title>
<link href="https://fonts.googleapis.com/css2?family=Lato:wght@400;700;900&display=swap" rel="stylesheet">
<style>
  :root {
    --brand-red: #c8101e;
    --ink: #1d1d1f;
    --rule: #6d6d6d;
    --card: #ffffff;
    --backdrop: #e4e4e4;
  }
  * { margin: 0; padding: 0; box-sizing: border-box; }
  html, body { width: 1200px; height: 675px; overflow: hidden; }
  body {
    background: var(--backdrop);
    font-family: "Lato", Arial, sans-serif;
    color: var(--ink);
    position: relative;
  }
  .card {
    position: absolute;
    left: 110px; top: 57px;
    width: 980px; height: 560px;
    background: var(--card);
    box-shadow: 0 6px 24px rgba(0,0,0,0.12);
    overflow: hidden;
  }
  .brand {
    position: absolute;
    right: 90px; top: 72px;
    display: flex; align-items: center; gap: 18px;
  }
  .brand-dot {
    width: 26px; height: 26px; border-radius: 50%;
    background: var(--brand-red);
  }
  .brand-name {
    font-weight: 900;
    font-size: 90px;
    letter-spacing: 4px;
    color: var(--brand-red);
    line-height: 1;
  }
  .divider {
    position: absolute;
    left: 140px; right: 50px; top: 232px;
    height: 1.5px; background: var(--rule);
  }
  .person { position: absolute; left: 140px; top: 268px; }
  .person-name {
    font-size: 40px; font-weight: 400;
    color: var(--brand-red); line-height: 1.1;
  }
  .person-title { font-size: 22px; margin-top: 4px; }
  .person-rule {
    position: absolute; left: 140px; top: 366px;
    width: 280px; height: 1.5px; background: var(--rule);
  }
  .contacts {
    position: absolute; left: 140px; top: 384px;
    list-style: none;
  }
  .contacts li {
    display: flex; align-items: center; gap: 14px;
    font-size: 21px; height: 27px;
  }
  .contacts svg { width: 18px; height: 18px; fill: var(--brand-red); flex: none; }
  .address {
    position: absolute; right: 80px; top: 376px;
    text-align: right; font-size: 22px; line-height: 1.2;
  }
  .footer-bands { position: absolute; left: 0; bottom: 0; width: 980px; height: 110px; }
</style>
</head>
<body>
  <div class="card">
    <div class="brand">
      <span class="brand-dot"></span>
      <span class="brand-name">ORQEL</span>
    </div>
    <div class="divider"></div>

    <div class="person">
      <div class="person-name">Mark Ellison</div>
      <div class="person-title">Manager</div>
    </div>
    <div class="person-rule"></div>

    <ul class="contacts">
      <li>
        <svg viewBox="0 0 24 24"><path d="M6.6 10.8a15 15 0 0 0 6.6 6.6l2.2-2.2c.3-.3.7-.4 1-.2 1.1.4 2.3.6 3.6.6.6 0 1 .4 1 1V20c0 .6-.4 1-1 1A17 17 0 0 1 3 4c0-.6.4-1 1-1h3.5c.6 0 1 .4 1 1 0 1.3.2 2.5.6 3.6.1.3 0 .7-.2 1z"/></svg>
        555 010 4800
      </li>
      <li>
        <svg viewBox="0 0 24 24"><path d="M7 2h10a2 2 0 0 1 2 2v16a2 2 0 0 1-2 2H7a2 2 0 0 1-2-2V4a2 2 0 0 1 2-2zm0 3v12h10V5zm5 13.5a1.2 1.2 0 1 0 0 2.4 1.2 1.2 0 0 0 0-2.4z"/></svg>
        555 010 4801
      </li>
      <li>
        <svg viewBox="0 0 24 24"><path d="M3 5h18a1 1 0 0 1 1 1v12a1 1 0 0 1-1 1H3a1 1 0 0 1-1-1V6a1 1 0 0 1 1-1zm1 2.3V17h16V7.3l-8 5.2z"/></svg>
        info@orqel-example.com
      </li>
      <li>
        <svg viewBox="0 0 24 24"><path d="M12 2a10 10 0 1 0 0 20 10 10 0 0 0 0-20zm6.9 6h-3a15 15 0 0 0-1.3-3.9A8 8 0 0 1 18.9 8zM12 4c.8 1.2 1.5 2.5 1.9 4h-3.8c.4-1.5 1.1-2.8 1.9-4zM4.3 14a8 8 0 0 1 0-4h3.4a16 16 0 0 0 0 4zm.8 2h3a15 15 0 0 0 1.3 3.9A8 8 0 0 1 5.1 16zm3-8h-3a8 8 0 0 1 4.3-3.9A15 15 0 0 0 8.1 8zM12 20c-.8-1.2-1.5-2.5-1.9-4h3.8c-.4 1.5-1.1 2.8-1.9 4zm2.3-6H9.7a14 14 0 0 1 0-4h4.6a14 14 0 0 1 0 4zm.3 5.9a15 15 0 0 0 1.3-3.9h3a8 8 0 0 1-4.3 3.9zm1.7-5.9a16 16 0 0 0 0-4h3.4a8 8 0 0 1 0 4z"/></svg>
        www.orqel-example.com
      </li>
    </ul>

    <div class="address">1450 Harbor Lane<br>Millbrook TX 70000</div>

    <svg class="footer-bands" viewBox="0 0 980 110" preserveAspectRatio="none" aria-hidden="true">
      <polygon points="0,62 700,62 760,14 780,14 720,74 0,74" fill="#1d1d1f"/>
      <polygon points="0,80 726,80 786,14 980,14 980,110 0,110" fill="var(--brand-red)"/>
    </svg>
  </div>
</body>
</html>
```